Corporate Power Point Template

Tarrowmead Group, Inc. produces and sells ready-mixed concrete, aggregates, and concrete-related products and services for the construction industry in the United States.

We are looking for a simple and sleek design that will look great on a projector, as well as when printed on paper. We prefer a lighter background color that will not waste ink when printed. We would also like to stay away from wavy banners, or over-the-top graphics that take away from usable space in the deck. Please use a variation of the color scheme in the "Brand Standards" file attached.

```html
<!DOCTYPE html>
<html lang="en">
<head>
<meta charset="utf-8">
<title>Tarrowmead Group, Inc. — Corporate Presentation Template</title>
<link href="https://fonts.googleapis.com/css2?family=Roboto:wght@300;400;500;700&display=swap" rel="stylesheet">
<style>
:root{
  --red:#c8102e;
  --ink:#1b1b1b;
  --black:#141414;
  --charcoal:#3b3b3d;
  --grey:#6f6f71;
  --mid:#8a8a8c;
  --soft:#b3b3b5;
  --line:#e1e1e3;
  --paper:#ffffff;
  --canvas:#d4d4d6;
}
*{box-sizing:border-box;margin:0;padding:0}
html,body{width:1200px;height:1144px;overflow:hidden;background:var(--canvas)}
body{position:relative;font-family:"Roboto",Arial,sans-serif;color:var(--ink)}
.icons{position:absolute;width:0;height:0}
.slide{position:absolute;width:398px;height:227px;background:var(--paper);overflow:hidden}
.title{position:absolute;left:17px;top:12px;font:300 18px/1 "Roboto",Arial,sans-serif;color:var(--ink);text-transform:uppercase;letter-spacing:.1px}
.title::after{content:"";position:absolute;left:0;top:23px;width:24px;height:1.5px;background:var(--red)}
.brand{position:absolute;right:15px;top:13px;display:flex;align-items:center;gap:3px;font:700 8px/1 "Roboto",Arial,sans-serif;color:#58595b;letter-spacing:.6px}
.brand::after{content:"";width:6px;height:6px;background:var(--red)}
.foot{position:absolute;left:0;right:0;bottom:0;height:10px;background:var(--grey)}
.foot .num{position:absolute;left:0;top:0;width:22px;height:10px;background:#e8e8ea;font:400 4.5px/10px "Roboto",Arial,sans-serif;color:#555;text-align:center}
.foot .copy{position:absolute;right:14px;top:0;font:300 3.8px/10px "Roboto",Arial,sans-serif;color:#e4e4e4}
.abs{position:absolute}
.lorem{font:300 4.6px/1.4 "Roboto",Arial,sans-serif;color:var(--soft)}
.lorem + .lorem{margin-top:4px}
.lead{font:300 8.5px/1.35 "Roboto",Arial,sans-serif;color:var(--ink)}
.center{text-align:center}
.label{font:400 5.5px/1.3 "Roboto",Arial,sans-serif;color:var(--grey);margin:4px 0 1px}
.label.red,.red{color:var(--red)}
.ico{width:100%;height:100%;fill:currentColor}
.ring{display:block;margin:0 auto;width:22px;height:22px;border-radius:50%;border:1.2px solid var(--grey);color:var(--grey);padding:4px}
.ring.is-red{border-color:var(--red);color:var(--red)}
.ring.is-dark{border-color:var(--black);color:var(--black)}
.dot{display:block;margin:0 auto;width:16px;height:16px;border-radius:50%;color:#fff;padding:3.5px}
.bg-red{background:var(--red)} .bg-grey{background:var(--mid)} .bg-black{background:var(--black)} .bg-char{background:var(--charcoal)}
.vrule{position:absolute;width:.6px;background:var(--line)}
.hrule{position:absolute;height:.8px;background:var(--red)}
.heading{font:300 8.5px/1.2 "Roboto",Arial,sans-serif;color:var(--ink);margin-bottom:2px}

/* pricing */
.band{position:absolute;left:0;right:0;top:113px;bottom:0;background:var(--grey)}
.plan-head{position:absolute;color:#fff;text-align:center;font:300 14px/1 "Roboto",Arial,sans-serif;padding-top:11px}
.plan-head small{display:block;font:300 3.6px/1 "Roboto",Arial,sans-serif;margin-top:2px}
.plan-head.is-featured{font-size:17px;padding-top:12px}
.plan-list{position:absolute;background:#fff;list-style:none;padding:6px 6px 0;box-shadow:0 0 3px rgba(0,0,0,.12)}
.plan-list li{font:300 4px/1 "Roboto",Arial,sans-serif;color:#777;text-align:center;padding:4.5px 0;border-bottom:.5px solid var(--line)}
.plan-list li:last-child{border-bottom:0}

/* video */
.video-title{position:absolute;left:17px;top:33px;font:300 17px/1.02 "Roboto",Arial,sans-serif;text-transform:uppercase}
.video-title::after{content:"";display:block;width:24px;height:1.5px;background:var(--red);margin-top:6px}
.monitor{position:absolute;left:125px;top:36px;width:223px;height:161px;background:#111;border-radius:5px 5px 0 0}
.monitor .screen{position:absolute;left:8px;top:8px;right:8px;bottom:23px;background:linear-gradient(160deg,#8fa3b6 0%,#6c7884 45%,#8a5a4c 70%,#5b5650 100%)}
.monitor .chin{position:absolute;left:0;right:0;bottom:0;height:23px;background:linear-gradient(#e9e9eb,#c9c9cc)}
.stand{position:absolute;left:213px;top:197px;width:48px;height:13px;background:linear-gradient(#cfcfd2,#e9e9eb);clip-path:polygon(18% 0,82% 0,100% 100%,0 100%)}

/* tiles */
.tile{position:absolute;top:86px;width:74px;height:96px;color:#fff;text-align:center;padding-top:20px}
.tile .dot{width:18px;height:18px;background:rgba(255,255,255,.92);color:var(--grey);padding:4px}
.tile h3{font:300 7px/1 "Roboto",Arial,sans-serif;margin:12px 0 4px}
.tile p{font:300 4.8px/1.3 "Roboto",Arial,sans-serif;padding:0 6px}

/* big rings */
.bigring{display:block;margin:0 auto;width:46px;height:46px;border-radius:50%;border:4px solid var(--red);color:var(--red);padding:10px}
.bigring.is-grey{border-color:var(--mid);color:var(--mid)}
.bigring.is-dark{border-color:var(--black);color:var(--black)}
.bigring.is-char{border-color:var(--charcoal);color:var(--charcoal)}
.colhead{font:400 6.2px/1 "Roboto",Arial,sans-serif;margin:7px 0 3px;text-transform:uppercase}

/* services */
.service{position:absolute;width:110px;display:flex;gap:5px}
.service .dot{flex:none;width:24px;height:24px;margin:0;padding:5.5px}
.service h4{font:400 4.6px/1 "Roboto",Arial,sans-serif;text-transform:uppercase;margin:1px 0 1.5px}
.service .lorem{font-size:4.1px;color:#9a9a9c}

/* divider */
.divider{background:var(--charcoal)}
.divider .big-name{position:absolute;right:28px;top:108px;font:700 22px/1 "Roboto",Arial,sans-serif;color:#fff;letter-spacing:1px}
.divider h2{position:absolute;right:28px;top:143px;font:300 17px/1 "Roboto",Arial,sans-serif;color:#fff;text-transform:uppercase}
.divider p{position:absolute;right:28px;top:164px;font:300 6px/1 "Roboto",Arial,sans-serif;color:#e6e6e6}

/* key points */
.keypoint{position:absolute;top:97px;width:56px;height:56px;border-radius:50%;color:#fff;text-align:center;padding-top:15px;font:300 5px/1.2 "Roboto",Arial,sans-serif}
.keypoint .ico{display:block;width:11px;height:11px;margin:0 auto 2px}

/* charts */
svg text{font-family:"Roboto",Arial,sans-serif}
.btn{position:absolute;left:25px;top:87px;width:89px;height:13px;background:var(--red);color:#fff;font:400 5.2px/13px "Roboto",Arial,sans-serif;text-align:center}
.chart-title{font:300 6px/1 "Roboto",Arial,sans-serif;color:var(--ink);text-align:center}

/* team */
.member{position:absolute;width:170px}
.photo{position:absolute;left:0;top:0;width:44px;height:44px;border-radius:50%}
.photo.a{background:radial-gradient(circle at 50% 40%,#c9a58a,#6a6f74 70%,#e8e8e8 71%)}
.photo.b{background:radial-gradient(circle at 50% 40%,#8a5a43,#a7a9ac 70%,#eeeeee 71%)}
.photo.c{background:radial-gradient(circle at 50% 40%,#e5c29a,#b08a5b 65%,#e6eef2 71%)}
.photo.d{background:radial-gradient(circle at 50% 40%,#d9a98b,#7f8a94 68%,#eeeeee 71%)}
.member .info{position:absolute;left:49px;top:-9px;width:120px}
.member h4{font:300 7.5px/1 "Roboto",Arial,sans-serif;color:var(--ink)}
.member .role{font:400 4.6px/1.2 "Roboto",Arial,sans-serif;color:var(--red)}
.member .cred{font:300 4px/1.2 "Roboto",Arial,sans-serif;color:#888}
.member ul{list-style:none;margin-top:1px}
.member li{font:300 4px/1.3 "Roboto",Arial,sans-serif;color:#999;padding-left:4px;position:relative}
.member li::before{content:"";position:absolute;left:0;top:1.8px;width:1.8px;height:1.8px;border-radius:50%;background:var(--red)}
</style>
</head>
<body>

<svg class="icons" aria-hidden="true">
  <symbol id="i-chart" viewBox="0 0 24 24"><rect x="4" y="13" width="3" height="7"/><rect x="10.5" y="9" width="3" height="11"/><rect x="17" y="5" width="3" height="15"/><rect x="3" y="20.5" width="18" height="1.5"/></symbol>
  <symbol id="i-crown" viewBox="0 0 24 24"><path d="M3 8l4.5 4L12 5l4.5 7L21 8l-2 10H5z"/><rect x="5" y="19" width="14" height="2"/></symbol>
  <symbol id="i-rocket" viewBox="0 0 24 24"><path d="M20.5 3.5s-5-.5-9 3.5L8 10.5l5.5 5.5 3.5-3.5c4-4 3.5-9 3.5-9zM15 7.5a1.5 1.5 0 110 3 1.5 1.5 0 010-3zM7 11l-4 1 2.5 2.5zM13 17l-1 4-2.5-2.5zM6 16l-3 5 5-3z"/></symbol>
  <symbol id="i-search" viewBox="0 0 24 24"><path fill-rule="evenodd" d="M10 3a7 7 0 015.6 11.2l4.9 4.9-1.4 1.4-4.9-4.9A7 7 0 1110 3zm0 2a5 5 0 100 10 5 5 0 000-10z"/></symbol>
  <symbol id="i-pencil" viewBox="0 0 24 24"><path d="M15.5 3.5l5 5L9 20H4v-5z"/></symbol>
  <symbol id="i-award" viewBox="0 0 24 24"><circle cx="12" cy="10" r="6.5"/><path d="M8 15l-2 7 3-1.5 2 2 1-5.5zM16 15l2 7-3-1.5-2 2-1-5.5z"/></symbol>
  <symbol id="i-heart" viewBox="0 0 24 24"><path d="M12 21l-7.5-7.5a4.8 4.8 0 016.8-6.8l.7.7.7-.7a4.8 4.8 0 016.8 6.8z"/></symbol>
  <symbol id="i-people" viewBox="0 0 24 24"><circle cx="9" cy="8" r="3"/><circle cx="16.5" cy="8.5" r="2.5"/><path d="M2.5 19c0-3.5 3-5.5 6.5-5.5s6.5 2 6.5 5.5zM16.5 19c0-2-.6-3.6-1.8-4.7.6-.2 1.2-.3 1.8-.3 2.8 0 5 1.7 5 4.5v.5z"/></symbol>
  <symbol id="i-device" viewBox="0 0 24 24"><path fill-rule="evenodd" d="M7 2h10a1.5 1.5 0 011.5 1.5v17A1.5 1.5 0 0117 22H7a1.5 1.5 0 01-1.5-1.5v-17A1.5 1.5 0 017 2zm1 3v12h8V5z"/></symbol>
</svg>

<!-- Row 1 -->
<section class="slide" style="left:0;top:0">
  <h2 class="title">Paragraph with three bullet</h2>
  <div class="brand">TARROWMEAD</div>
  <p class="abs lead" style="left:19px;top:60px;width:330px">This is place for your header text. Insert your text here, just replace this text with your own text</p>
  <div class="abs" style="left:20px;top:104px;width:105px">
    <p class="lorem">Lorem ipsum dolor sit amet, consectetur adipiscing elit, sed do eiusmod tempor incididunt ut labore et dolore magna aliqua. Ut enim ad minim veniam, quis nostrud exercitation ullamco laboris nisi ut aliquip ex ea commodo consequat.</p>
    <p class="lorem">Duis aute irure dolor in reprehenderit in voluptate velit esse cillum dolore eu fugiat nulla pariatur excepteur occaecat.</p>
  </div>
  <span class="vrule" style="left:142px;top:96px;height:106px"></span>
  <div class="abs center" style="left:154px;top:92px;width:70px">
    <span class="ring is-red"><svg class="ico"><use href="#i-chart"/></svg></span>
    <p class="label red">Your Text Here</p>
    <p class="lorem">Lorem ipsum dolor sit amet, consectetur adipiscing elit, sed do eiusmod tempor incididunt ut labore et aliqua.</p>
    <p class="lorem">Ut enim ad minim veniam, quis nostrud exercitation ullamco laboris nisi ut commodo consequat.</p>
  </div>
  <span class="vrule" style="left:230px;top:96px;height:106px"></span>
  <div class="abs center" style="left:235px;top:92px;width:70px">
    <span class="ring"><svg class="ico"><use href="#i-crown"/></svg></span>
    <p class="label">Your Text Here</p>
    <p class="lorem">Lorem ipsum dolor sit amet, consectetur adipiscing elit, sed do eiusmod tempor incididunt ut labore et aliqua.</p>
    <p class="lorem">Ut enim ad minim veniam, quis nostrud exercitation ullamco laboris nisi ut commodo consequat.</p>
  </div>
  <span class="vrule" style="left:310px;top:96px;height:106px"></span>
  <div class="abs center" style="left:313px;top:92px;width:70px">
    <span class="ring is-dark"><svg class="ico"><use href="#i-rocket"/></svg></span>
    <p class="label">Your Text Here</p>
    <p class="lorem">Lorem ipsum dolor sit amet, consectetur adipiscing elit, sed do eiusmod tempor incididunt ut labore et aliqua.</p>
    <p class="lorem">Ut enim ad minim veniam, quis nostrud exercitation ullamco laboris nisi ut commodo consequat.</p>
  </div>
  <div class="foot"><span class="num">31</span><span class="copy">© 2017 TARROWMEAD All rights reserved</span></div>
</section>

<section class="slide" style="left:400px;top:0">
  <h2 class="title">Multiple column area</h2>
  <div class="brand">TARROWMEAD</div>
  <div class="abs center" style="left:19px;top:62px;width:66px"><span class="dot bg-red"><svg class="ico"><use href="#i-award"/></svg></span><p class="label red">Your Text Here</p><p class="lorem">Lorem ipsum consectetur adipiscing elit.</p></div>
  <div class="abs center" style="left:92px;top:62px;width:66px"><span class="dot bg-grey"><svg class="ico"><use href="#i-rocket"/></svg></span><p class="label">Your Text Here</p><p class="lorem">Lorem ipsum consectetur adipiscing elit.</p></div>
  <div class="abs center" style="left:165px;top:62px;width:66px"><span class="dot bg-black"><svg class="ico"><use href="#i-search"/></svg></span><p class="label" style="color:var(--ink)">Your Text Here</p><p class="lorem">Lorem ipsum consectetur adipiscing elit.</p></div>
  <div class="abs center" style="left:239px;top:62px;width:66px"><span class="dot bg-grey"><svg class="ico"><use href="#i-pencil"/></svg></span><p class="label">Your Text Here</p><p class="lorem">Lorem ipsum consectetur adipiscing elit.</p></div>
  <div class="abs center" style="left:312px;top:62px;width:66px"><span class="dot bg-red"><svg class="ico"><use href="#i-chart"/></svg></span><p class="label red">Your Text Here</p><p class="lorem">Lorem ipsum consectetur adipiscing elit.</p></div>
  <span class="hrule" style="left:28px;top:121px;width:344px"></span>
  <div class="abs" style="left:28px;top:137px;width:165px">
    <p class="heading">Heading Goes Here</p>
    <p class="lorem">Lorem ipsum dolor sit amet, consectetur adipiscing elit, sed do eiusmod tempor incididunt ut labore et commodo consequat dolore magna aliqua.</p>
    <p class="lorem">Duis aute irure dolor in reprehenderit in voluptate velit esse cillum dolore eu fugiat nulla pariatur.</p>
  </div>
  <div class="abs" style="left:215px;top:137px;width:165px">
    <p class="heading">Heading Goes Here</p>
    <p class="lorem">Lorem ipsum dolor sit amet, consectetur adipiscing elit, sed do eiusmod tempor incididunt ut labore et commodo consequat dolore magna aliqua.</p>
    <p class="lorem">Duis aute irure dolor in reprehenderit in voluptate velit esse cillum dolore eu fugiat nulla pariatur.</p>
  </div>
  <div class="foot"><span class="num">32</span><span class="copy">© 2017 TARROWMEAD All rights reserved</span></div>
</section>

<section class="slide" style="left:800px;top:0">
  <h2 class="title">Monthly subscription</h2>
  <div class="brand">TARROWMEAD</div>
  <div class="band"></div>
  <div class="plan-head" style="left:58px;top:78px;width:80px;height:36px;background:var(--black)">$300<small>per month</small></div>
  <ul class="plan-list" style="left:58px;top:114px;width:80px;height:74px"><li>Single Edition</li><li>30gb Cloud Service</li><li>3 User</li><li>Free Update</li></ul>
  <div class="plan-head is-featured" style="left:148px;top:72px;width:102px;height:42px;background:var(--red)">$900<small>per month</small></div>
  <ul class="plan-list" style="left:148px;top:114px;width:102px;height:81px;padding-top:8px"><li>Business Edition</li><li>60gb Cloud Service</li><li>6 User</li><li>Free Update</li></ul>
  <div class="plan-head" style="left:260px;top:78px;width:79px;height:36px;background:var(--mid)">$400<small>per month</small></div>
  <ul class="plan-list" style="left:260px;top:114px;width:79px;height:74px"><li>Single Edition</li><li>30gb Cloud Service</li><li>3 User</li><li>Free Update</li></ul>
  <div class="foot" style="background:#5e5e60"><span class="num">33</span><span class="copy">© 2017 TARROWMEAD All rights reserved</span></div>
</section>

<!-- Row 2 -->
<section class="slide" style="left:0;top:229px">
  <h2 class="video-title">Video title<br>goes here</h2>
  <div class="brand">TARROWMEAD</div>
  <div class="abs" style="left:18px;top:90px;width:95px">
    <p class="lorem">Lorem ipsum dolor sit amet, consectetur adipiscing elit, sed do eiusmod tempor incididunt ut labore et commodo consequat dolore magna aliqua.</p>
    <p class="lorem">Duis aute irure dolor in reprehenderit in voluptate velit esse cillum dolore eu fugiat nulla pariatur.</p>
    <p class="lorem">Ut enim ad minim veniam, quis nostrud exercitation ullamco laboris.</p>
  </div>
  <div class="monitor">
    <div class="screen" role="img" aria-label="Video still of a ready-mix concrete truck at a building construction site"></div>
    <div class="chin"></div>
  </div>
  <div class="stand"></div>
  <div class="foot"><span class="num">34</span><span class="copy">© 2017 TARROWMEAD All rights reserved</span></div>
</section>

<section class="slide" style="left:400px;top:229px">
  <h2 class="title">Four column area</h2>
  <div class="brand">TARROWMEAD</div>
  <p class="abs lorem" style="left:33px;top:62px;width:340px;font-size:5px;color:#8e8e90">Lorem ipsum dolor sit amet, consectetur adipiscing elit, sed do eiusmod tempor incididunt ut labore et dolore magna aliqua. Ut enim ad minim veniam, quis nostrud exercitation ullamco laboris nisi ut aliquip ex ea commodo consequat.</p>
  <div class="tile bg-red" style="left:30px"><span class="dot" style="color:var(--red)"><svg class="ico"><use href="#i-crown"/></svg></span><h3>Your Text Here</h3><p>Lorem Ipsum Dolor Sit Consectetur Adipiscing Elit.</p></div>
  <div class="tile bg-grey" style="left:118px"><span class="dot"><svg class="ico"><use href="#i-rocket"/></svg></span><h3>Your Text Here</h3><p>Lorem Ipsum Dolor Sit Consectetur Adipiscing Elit.</p></div>
  <div class="tile bg-black" style="left:206px"><span class="dot" style="color:var(--black)"><svg class="ico"><use href="#i-award"/></svg></span><h3>Your Text Here</h3><p>Lorem Ipsum Dolor Sit Consectetur Adipiscing Elit.</p></div>
  <div class="tile bg-char" style="left:294px"><span class="dot" style="color:var(--charcoal)"><svg class="ico"><use href="#i-chart"/></svg></span><h3>Your Text Here</h3><p>Lorem Ipsum Dolor Sit Consectetur Adipiscing Elit.</p></div>
  <div class="foot"><span class="num">35</span><span class="copy">© 2017 TARROWMEAD All rights reserved</span></div>
</section>

<section class="slide" style="left:800px;top:229px">
  <h2 class="title">Four column area</h2>
  <div class="brand">TARROWMEAD</div>
  <p class="abs lorem center" style="left:50px;top:52px;width:300px;font-size:5px;color:#8e8e90">Lorem ipsum dolor sit amet, consectetur adipiscing elit, sed do eiusmod tempor incididunt ut labore et dolore magna aliqua. Ut enim ad minim veniam, quis nostrud exercitation ullamco laboris nisi ut aliquip ex ea commodo consequat.</p>
  <div class="abs center" style="left:48px;top:80px;width:60px"><span class="bigring"><svg class="ico"><use href="#i-chart"/></svg></span><p class="colhead red">Column 1</p><p class="lorem">Lorem ipsum dolor sit amet, consectetur adipiscing elit, sed do eiusmod tempor incididunt ut labore et dolore magna aliqua.</p></div>
  <span class="vrule" style="left:118px;top:80px;height:100px"></span>
  <div class="abs center" style="left:128px;top:80px;width:60px"><span class="bigring is-grey"><svg class="ico"><use href="#i-crown"/></svg></span><p class="colhead" style="color:var(--grey)">Column 2</p><p class="lorem">Lorem ipsum dolor sit amet, consectetur adipiscing elit, sed do eiusmod tempor incididunt ut labore et dolore magna aliqua.</p></div>
  <span class="vrule" style="left:199px;top:80px;height:100px"></span>
  <div class="abs center" style="left:209px;top:80px;width:60px"><span class="bigring is-dark"><svg class="ico"><use href="#i-rocket"/></svg></span><p class="colhead" style="color:var(--black)">Column 3</p><p class="lorem">Lorem ipsum dolor sit amet, consectetur adipiscing elit, sed do eiusmod tempor incididunt ut labore et dolore magna aliqua.</p></div>
  <span class="vrule" style="left:279px;top:80px;height:100px"></span>
  <div class="abs center" style="left:289px;top:80px;width:60px"><span class="bigring is-char"><svg class="ico"><use href="#i-award"/></svg></span><p class="colhead" style="color:var(--charcoal)">Column 4</p><p class="lorem">Lorem ipsum dolor sit amet, consectetur adipiscing elit, sed do eiusmod tempor incididunt ut labore et dolore magna aliqua.</p></div>
  <div class="foot"><span class="num">36</span><span class="copy">© 2017 TARROWMEAD All rights reserved</span></div>
</section>

<!-- Row 3 -->
<section class="slide" style="left:0;top:458px">
  <h2 class="title">Our services</h2>
  <div class="brand">TARROWMEAD</div>
  <div class="service" style="left:50px;top:55px"><span class="dot bg-red"><svg class="ico"><use href="#i-award"/></svg></span><div><h4 class="red">Brand Apparels</h4><p class="lorem">Lorem ipsum dolor sit amet, consectetur adipiscing elit, sed diam nonummy nibh euismod tincidunt ut laoreet dolore magna aliquam erat volutpat.</p></div></div>
  <div class="service" style="left:160px;top:55px"><span class="dot bg-grey"><svg class="ico"><use href="#i-award"/></svg></span><div><h4 style="color:var(--grey)">Brand Apparels</h4><p class="lorem">Lorem ipsum dolor sit amet, consectetur adipiscing elit, sed diam nonummy nibh euismod tincidunt ut laoreet dolore magna aliquam erat volutpat.</p></div></div>
  <div class="service" style="left:268px;top:55px"><span class="dot bg-black"><svg class="ico"><use href="#i-award"/></svg></span><div><h4 style="color:var(--black)">Brand Apparels</h4><p class="lorem">Lorem ipsum dolor sit amet, consectetur adipiscing elit, sed diam nonummy nibh euismod tincidunt ut laoreet dolore magna aliquam erat volutpat.</p></div></div>
  <div class="service" style="left:50px;top:102px"><span class="dot bg-grey"><svg class="ico"><use href="#i-device"/></svg></span><div><h4 style="color:var(--grey)">Print Services</h4><p class="lorem">Ut wisi enim ad minim veniam, quis nostrud exerci tation ullamcorper suscipit lobortis nisl ut aliquip ex ea commodo consequat. Duis autem vel eum esse molestie consequat.</p></div></div>
  <div class="service" style="left:160px;top:102px"><span class="dot bg-black"><svg class="ico"><use href="#i-device"/></svg></span><div><h4 style="color:var(--black)">Print Services</h4><p class="lorem">Ut wisi enim ad minim veniam, quis nostrud exerci tation ullamcorper suscipit lobortis nisl ut aliquip ex ea commodo consequat.</p></div></div>
  <div class="service" style="left:268px;top:102px"><span class="dot bg-red"><svg class="ico"><use href="#i-device"/></svg></span><div><h4 class="red">Print Services</h4><p class="lorem">Ut wisi enim ad minim veniam, quis nostrud exerci tation ullamcorper suscipit lobortis nisl ut aliquip ex ea commodo consequat. Duis autem vel eum esse molestie consequat.</p></div></div>
  <div class="service" style="left:50px;top:151px"><span class="dot bg-black"><svg class="ico"><use href="#i-chart"/></svg></span><div><h4 style="color:var(--black)">Pop/Pos Services</h4><p class="lorem">Ut wisi enim ad minim veniam, quis nostrud exerci tation ullamcorper suscipit lobortis nisl ut aliquip ex ea commodo esse molestie consequat.</p></div></div>
  <div class="service" style="left:160px;top:151px"><span class="dot bg-red"><svg class="ico"><use href="#i-chart"/></svg></span><div><h4 class="red">Web Services</h4><p class="lorem">Ut wisi enim ad minim veniam, quis nostrud exerci tation ullamcorper suscipit lobortis nisl ut aliquip ex ea commodo. Duis autem vel eum iriure dolor consequat.</p></div></div>
  <div class="service" style="left:268px;top:151px"><span class="dot bg-grey"><svg class="ico"><use href="#i-chart"/></svg></span><div><h4 style="color:var(--grey)">Pop/Pos Services</h4><p class="lorem">Ut wisi enim ad minim veniam, quis nostrud exerci tation ullamcorper suscipit lobortis nisl ut aliquip ex ea commodo esse molestie consequat.</p></div></div>
  <div class="foot"><span class="num">37</span><span class="copy">© 2017 TARROWMEAD All rights reserved</span></div>
</section>

<section class="slide divider" style="left:400px;top:458px">
  <div class="big-name">TARROWMEAD</div>
  <h2>Divider title here</h2>
  <p>your subtitle goes here</p>
</section>

<section class="slide" style="left:800px;top:458px">
  <h2 class="title">Key points area</h2>
  <div class="brand">TARROWMEAD</div>
  <p class="abs lorem" style="left:25px;top:66px;width:350px;font-size:5px;color:#8e8e90">Lorem ipsum dolor sit amet, consectetur adipiscing elit, sed do eiusmod tempor incididunt ut labore et dolore magna aliqua. Ut enim ad minim veniam, quis nostrud exercitation ullamco laboris nisi ut aliquip ex ea commodo consequat.</p>
  <div class="keypoint bg-red" style="left:75px"><svg class="ico"><use href="#i-people"/></svg>Lorem<br>ipsum</div>
  <div class="keypoint bg-grey" style="left:123px"><svg class="ico"><use href="#i-pencil"/></svg>Lorem<br>ipsum</div>
  <div class="keypoint bg-black" style="left:171px"><svg class="ico"><use href="#i-chart"/></svg>Lorem<br>ipsum</div>
  <div class="keypoint bg-grey" style="left:219px"><svg class="ico"><use href="#i-heart"/></svg>Lorem<br>ipsum</div>
  <div class="keypoint bg-red" style="left:266px"><svg class="ico"><use href="#i-crown"/></svg>Lorem<br>ipsum</div>
  <p class="abs lorem center" style="left:70px;top:163px;width:260px;font-size:5px;color:#8e8e90">Lorem ipsum dolor sit amet, consectetur adipiscing elit, sed do eiusmod tempor incididunt ut labore et dolore magna aliqua. Ut enim ad minim veniam, quis nostrud exercitation ullamco laboris nisi ut aliquip ex ea commodo consequat.</p>
  <div class="foot"><span class="num">39</span><span class="copy">© 2017 TARROWMEAD All rights reserved</span></div>
</section>

<!-- Row 4 -->
<section class="slide" style="left:0;top:687px">
  <h2 class="title">Workflow area</h2>
  <div class="brand">TARROWMEAD</div>
  <p class="abs lorem" style="left:30px;top:60px;width:345px;font-size:5px;color:#8e8e90">Lorem ipsum dolor sit amet, consectetur adipiscing elit, sed do eiusmod tempor incididunt ut labore et dolore magna aliqua. Ut enim ad minim veniam, quis nostrud exercitation ullamco laboris nisi ut aliquip ex ea commodo consequat.</p>
  <svg class="abs" style="left:0;top:0" width="398" height="227" viewBox="0 0 398 227">
    <g fill="none" stroke-width="16">
      <path d="M34 135a33 33 0 0166 0" stroke="var(--mid)"/>
      <path d="M100 135a33 33 0 0066 0" stroke="var(--red)"/>
      <path d="M166 135a33 33 0 0166 0" stroke="var(--mid)"/>
      <path d="M232 135a33 33 0 0066 0" stroke="var(--red)"/>
      <path d="M298 135a33 33 0 0166 0" stroke="var(--mid)"/>
    </g>
    <g font-size="4.5" text-anchor="middle">
      <circle cx="67" cy="124" r="5.5" fill="#fff" stroke="#ddd" stroke-width=".5"/><text x="67" y="125.6" fill="#555">1</text>
      <circle cx="133" cy="145" r="5.5" fill="var(--red)" stroke="#fff" stroke-width=".8"/><text x="133" y="146.6" fill="#fff">2</text>
      <circle cx="199" cy="124" r="5.5" fill="#fff" stroke="#ddd" stroke-width=".5"/><text x="199" y="125.6" fill="#555">3</text>
      <circle cx="265" cy="145" r="5.5" fill="var(--red)" stroke="#fff" stroke-width=".8"/><text x="265" y="146.6" fill="#fff">4</text>
      <circle cx="331" cy="124" r="5.5" fill="#fff" stroke="#ddd" stroke-width=".5"/><text x="331" y="125.6" fill="#555">5</text>
    </g>
    <g font-size="6" font-weight="300" text-anchor="middle">
      <text x="67" y="142" fill="var(--ink)">Data 1</text>
      <text x="199" y="142" fill="var(--ink)">Data 3</text>
      <text x="331" y="142" fill="var(--ink)">Data 5</text>
      <text x="133" y="97" fill="var(--red)">Data 2</text>
      <text x="265" y="97" fill="var(--red)">Data 4</text>
    </g>
    <g font-size="4.2" font-weight="300" fill="#b8b8ba" text-anchor="middle">
      <text x="67" y="149">Lorem ipsum dolor</text><text x="67" y="154">sit amet,</text><text x="67" y="159">consectetur</text><text x="67" y="164">adipiscing elit.</text>
      <text x="199" y="149">Lorem ipsum dolor</text><text x="199" y="154">sit amet,</text><text x="199" y="159">consectetur</text><text x="199" y="164">adipiscing elit.</text>
      <text x="331" y="149">Lorem ipsum dolor</text><text x="331" y="154">sit amet,</text><text x="331" y="159">consectetur</text><text x="331" y="164">adipiscing elit.</text>
      <text x="133" y="103">Lorem ipsum dolor</text><text x="133" y="108">sit amet,</text><text x="133" y="113">consectetur</text><text x="133" y="118">adipiscing elit.</text>
      <text x="265" y="103">Lorem ipsum dolor</text><text x="265" y="108">sit amet,</text><text x="265" y="113">consectetur</text><text x="265" y="118">adipiscing elit.</text>
    </g>
  </svg>
  <div class="foot"><span class="num">40</span><span class="copy">© 2017 TARROWMEAD All rights reserved</span></div>
</section>

<section class="slide" style="left:400px;top:687px">
  <h2 class="title">Timeline</h2>
  <div class="brand">TARROWMEAD</div>
  <svg class="abs" style="left:0;top:0" width="398" height="227" viewBox="0 0 398 227">
    <g stroke="#9a9a9c" stroke-width=".6">
      <line x1="35" y1="107" x2="354" y2="107"/>
      <line x1="102" y1="83" x2="102" y2="107"/><line x1="198" y1="83" x2="198" y2="107"/><line x1="293" y1="83" x2="293" y2="107"/>
      <line x1="149" y1="107" x2="149" y2="122"/><line x1="246" y1="107" x2="246" y2="122"/>
    </g>
    <g fill="#555"><circle cx="102" cy="107" r="1.3"/><circle cx="149" cy="107" r="1.3"/><circle cx="198" cy="107" r="1.3"/><circle cx="246" cy="107" r="1.3"/><circle cx="293" cy="107" r="1.3"/></g>
    <path d="M346 124c4 6 2 12-4 15" fill="none" stroke="#777" stroke-width=".6"/>
    <g text-anchor="middle">
      <circle cx="53" cy="102" r="21" fill="var(--red)" stroke="#fff" stroke-width="1.5"/>
      <circle cx="102" cy="62" r="21" fill="var(--mid)" stroke="#fff" stroke-width="1.5"/>
      <circle cx="149" cy="143" r="21" fill="var(--black)" stroke="#fff" stroke-width="1.5"/>
      <circle cx="198" cy="62" r="21" fill="var(--charcoal)" stroke="#fff" stroke-width="1.5"/>
      <circle cx="246" cy="143" r="21" fill="var(--black)" stroke="#fff" stroke-width="1.5"/>
      <circle cx="293" cy="62" r="21" fill="var(--mid)" stroke="#fff" stroke-width="1.5"/>
      <circle cx="341" cy="102" r="21" fill="var(--red)" stroke="#fff" stroke-width="1.5"/>
      <g fill="#fff" font-size="9" font-weight="300">
        <text x="53" y="103">2013</text><text x="102" y="63">2014</text><text x="149" y="144">2015</text><text x="198" y="63">2016</text><text x="246" y="144">2017</text><text x="293" y="63">2018</text><text x="341" y="103">2019</text>
      </g>
      <g fill="#fff" font-size="3.4">
        <text x="53" y="108">Your Text</text><text x="53" y="112">Goes Here</text>
        <text x="102" y="68">Your Text</text><text x="102" y="72">Goes Here</text>
        <text x="149" y="149">Your Text</text><text x="149" y="153">Goes Here</text>
        <text x="198" y="68">Your Text</text><text x="198" y="72">Goes Here</text>
        <text x="246" y="149">Your Text</text><text x="246" y="153">Goes Here</text>
        <text x="293" y="68">Your Text</text><text x="293" y="72">Goes Here</text>
        <text x="341" y="108">Your Text</text><text x="341" y="112">Goes Here</text>
      </g>
    </g>
  </svg>
  <div class="abs" style="left:17px;top:177px;width:175px"><p class="heading" style="font-size:7px">Your Text Goes Here</p><p class="lorem">Lorem ipsum dolor sit amet, consectetur adipiscing elit, sed do eiusmod tempor incididunt ut labore et dolore magna aliqua.</p></div>
  <div class="abs center" style="left:288px;top:141px;width:80px"><p class="heading" style="font-size:7px">Your Text Goes Here</p><p class="lorem">Lorem ipsum dolor sit amet, consectetur adipiscing elit, sed do eiusmod tempor incididunt ut labore et dolore magna aliqua.</p></div>
  <div class="foot"><span class="num">41</span><span class="copy">© 2017 TARROWMEAD All rights reserved</span></div>
</section>

<section class="slide" style="left:800px;top:687px">
  <h2 class="title">This is line chart slide</h2>
  <div class="brand">TARROWMEAD</div>
  <div class="btn">CREATIVE TEXT HERE</div>
  <p class="abs lorem" style="left:29px;top:120px;width:100px;font-size:5.2px;color:#8e8e90"><span style="color:#444">Lorem Ipsum dolor</span> sit amet, consectetur adipiscing elit, sed do eiusmod tempor incididunt ut labore et commodo consequat dolore magna aliqua.</p>
  <svg class="abs" style="left:0;top:0" width="398" height="227" viewBox="0 0 398 227">
    <g font-size="4" fill="#888" text-anchor="end">
      <text x="167" y="181">0</text><text x="167" y="169">0.5</text><text x="167" y="156">1</text><text x="167" y="144">1.5</text><text x="167" y="132">2</text><text x="167" y="119">2.5</text><text x="167" y="107">3</text><text x="167" y="95">3.5</text><text x="167" y="82">4</text><text x="167" y="70">4.5</text><text x="167" y="57">5</text>
    </g>
    <line x1="172" y1="179" x2="376" y2="179" stroke="#d0d0d2" stroke-width=".5"/>
    <g font-size="4" fill="#888" text-anchor="middle">
      <text x="197" y="189">Category 1</text><text x="248" y="189">Category 2</text><text x="299" y="189">Category 3</text><text x="351" y="189">Category 4</text>
    </g>
    <polyline points="197,73 248,117 299,93 351,68" fill="none" stroke="var(--grey)" stroke-width="1.3"/>
    <polyline points="197,122 248,71 299,135 351,110" fill="none" stroke="var(--red)" stroke-width="1.3"/>
    <g fill="var(--grey)"><circle cx="197" cy="73" r="1.6"/><circle cx="248" cy="117" r="1.6"/><circle cx="299" cy="93" r="1.6"/><circle cx="351" cy="68" r="1.6"/></g>
    <g fill="var(--red)"><circle cx="197" cy="122" r="1.6"/><circle cx="248" cy="71" r="1.6"/><circle cx="299" cy="135" r="1.6"/><circle cx="351" cy="110" r="1.6"/></g>
  </svg>
  <div class="foot"><span class="num">42</span><span class="copy">© 2017 TARROWMEAD All rights reserved</span></div>
</section>

<!-- Row 5 -->
<section class="slide" style="left:0;top:916px">
  <h2 class="title">Market performance</h2>
  <div class="brand">TARROWMEAD</div>
  <svg class="abs" style="left:0;top:0" width="398" height="227" viewBox="0 0 398 227">
    <g font-size="4.5" fill="#555">
      <rect x="72" y="45" width="3" height="3" fill="var(--red)"/><text x="76.5" y="48">Profit</text>
      <rect x="94" y="45" width="3" height="3" fill="var(--grey)"/><text x="98.5" y="48">Cost</text>
      <rect x="113" y="45" width="3" height="3" fill="var(--black)"/><text x="117.5" y="48">Sales</text>
      <rect x="267" y="45" width="3" height="3" fill="var(--black)"/><text x="271.5" y="48">Profit</text>
      <rect x="289" y="45" width="3" height="3" fill="var(--grey)"/><text x="293.5" y="48">Cost</text>
      <rect x="308" y="45" width="3" height="3" fill="var(--red)"/><text x="312.5" y="48">Sales</text>
    </g>
    <polygon points="28,143 170,143 176,139 34,139" fill="#ececee"/>
    <polygon points="224,143 366,143 372,139 230,139" fill="#ececee"/>
    <g>
      <rect x="32" y="88" width="7" height="55" fill="var(--red)"/><rect x="40" y="94" width="7" height="49" fill="var(--grey)"/><rect x="48" y="109" width="7" height="34" fill="var(--black)"/>
      <rect x="69" y="103" width="7" height="40" fill="var(--red)"/><rect x="77" y="105" width="7" height="38" fill="var(--grey)"/><rect x="85" y="117" width="7" height="26" fill="var(--black)"/>
      <rect x="106" y="84" width="7" height="59" fill="var(--red)"/><rect x="114" y="89" width="7" height="54" fill="var(--grey)"/><rect x="122" y="125" width="7" height="18" fill="var(--black)"/>
      <rect x="143" y="60" width="7" height="83" fill="var(--red)"/><rect x="151" y="84" width="7" height="59" fill="var(--grey)"/><rect x="159" y="77" width="7" height="66" fill="var(--black)"/>

      <rect x="228" y="88" width="7" height="55" fill="var(--black)"/><rect x="236" y="95" width="7" height="48" fill="var(--grey)"/><rect x="244" y="108" width="7" height="35" fill="var(--red)"/>
      <rect x="265" y="103" width="7" height="40" fill="var(--black)"/><rect x="273" y="105" width="7" height="38" fill="var(--grey)"/><rect x="281" y="117" width="7" height="26" fill="var(--red)"/>
      <rect x="302" y="86" width="7" height="57" fill="var(--black)"/><rect x="310" y="89" width="7" height="54" fill="var(--grey)"/><rect x="318" y="123" width="7" height="20" fill="var(--red)"/>
      <rect x="339" y="61" width="7" height="82" fill="var(--black)"/><rect x="347" y="84" width="7" height="59" fill="var(--grey)"/><rect x="355" y="77" width="7" height="66" fill="var(--red)"/>
    </g>
    <g font-size="4.8" fill="#555" text-anchor="middle">
      <text x="43" y="151">2011</text><text x="80" y="151">2012</text><text x="117" y="151">2013</text><text x="154" y="151">2014</text>
      <text x="239" y="151">2011</text><text x="276" y="151">2012</text><text x="313" y="151">2013</text><text x="350" y="151">2014</text>
    </g>
  </svg>
  <div class="abs" style="left:28px;top:161px;width:148px"><p class="chart-title">Income</p><p class="lorem center" style="font-size:4.6px;color:#8e8e90;margin-top:3px">Nullam eu tempor purus. Nunc a leo magna, sit amet consequat risus. Etiam faucibus tortor a ipsum vehicula sed hendrerit eros suscipit. Mauris quam dolor, cursus at porta et, luctus eget purus.</p></div>
  <div class="abs" style="left:224px;top:161px;width:148px"><p class="chart-title">Cost Efficiency</p><p class="lorem center" style="font-size:4.6px;color:#8e8e90;margin-top:3px">Nullam eu tempor purus. Nunc a leo magna, sit amet consequat risus. Etiam faucibus tortor a ipsum vehicula sed hendrerit eros suscipit. Mauris quam dolor, cursus at porta et, luctus eget purus.</p></div>
  <div class="foot"><span class="num">43</span><span class="copy">© 2017 TARROWMEAD All rights reserved</span></div>
</section>

<section class="slide" style="left:400px;top:916px">
  <h2 class="title">Our team</h2>
  <div class="brand">TARROWMEAD</div>
  <div class="member" style="left:24px;top:55px">
    <div class="photo a" role="img" aria-label="Portrait photo of Michael Doe"></div>
    <div class="info"><h4>Michael Doe</h4><p class="role">CEO</p><p class="cred">MSMPTI, MBA and CIMA Dip PM</p>
      <ul><li>Lorem ipsum dolor sit amet, consectetur adipiscing elit</li><li>sed do eiusmod tempor incididunt ut labore et dolore magna aliqua.</li><li>Ut enim ad minim veniam, quis nostrud exercitation</li></ul></div>
  </div>
  <div class="member" style="left:200px;top:55px">
    <div class="photo b" role="img" aria-label="Portrait photo of James Doe"></div>
    <div class="info"><h4>James Doe</h4><p class="role">Manager</p><p class="cred">M.B.A</p>
      <ul><li>Lorem ipsum dolor sit amet, consectetur adipiscing elit</li><li>sed do eiusmod tempor incididunt ut labore et dolore magna aliqua.</li><li>Ut enim ad minim veniam, quis nostrud exercitation</li></ul></div>
  </div>
  <div class="member" style="left:24px;top:128px">
    <div class="photo c" role="img" aria-label="Portrait photo of Jane Doe"></div>
    <div class="info"><h4>Jane Doe</h4><p class="role">Doctor of Chemistry</p><p class="cred">M.B.A</p>
      <ul><li>Lorem ipsum dolor sit amet, consectetur adipiscing elit</li><li>sed do eiusmod tempor incididunt ut labore et dolore magna aliqua.</li><li>Ut enim ad minim veniam, quis nostrud exercitation</li></ul></div>
  </div>
  <div class="member" style="left:203px;top:128px">
    <div class="photo d" role="img" aria-label="Portrait photo of John Doe"></div>
    <div class="info"><h4>John Doe</h4><p class="role">Doctor of Physical</p><p class="cred">Professor</p>
      <ul><li>Lorem ipsum dolor sit amet, consectetur adipiscing elit</li><li>sed do eiusmod tempor incididunt ut labore et dolore magna aliqua.</li><li>Ut enim ad minim veniam, quis nostrud exercitation</li></ul></div>
  </div>
  <div class="foot"><span class="num">44</span><span class="copy">© 2017 TARROWMEAD All rights reserved</span></div>
</section>

<section class="slide" style="left:800px;top:916px">
  <h2 class="title">Your blank slide</h2>
  <div class="brand">TARROWMEAD</div>
  <div class="foot"><span class="num">45</span><span class="copy">© 2017 TARROWMEAD All rights reserved</span></div>
</section>

</body>
</html>
```